Responsive, beautiful email sign-up process pages

My client wants to re-imagine their email newsletter sign up process. The funnel currently starts in the first panel of their home page carousel at:

https://thriftbeacon.co.uk/

It is also featured in the right side of the footer.

I would like to start, what could become a full template re-design project by optimising this crucial user journey. I am attaching the screenshots from the current user journey below and it would be great to get some designs that improve on the look and feel.

Thank you,
Dorian

Target Market(s)

People who want to maximise the interest rate they receive on their cash savings.

Industry/Entity Type

Financial Service

Coding

Coded - Design and coding required

Number of Pages Required

4 page

Font styles to use
Sans Serif

Requirements
Must have
• A well designed, responsive design for all of the elements of the user journey funnel that works well on desktop, laptop, tablet and phone. The site is currently using Bootstrap 3.* for the responsive templates, so it would be useful to continue leveraging these libraries, but in a much more visually appealing way.
• It is felt that the current overall site is dull and unprofessional, so we are using this as a way of showing how much better it could be, which should lead to a sitewide "facelift".
Nice to have
• Creative use of css, svg and javascript to optimise the user experience on all target platforms.
Should not have
• Non-responsive designs.

```html
<!DOCTYPE html>
<html lang="en">
<head>
<meta charset="utf-8">
<title>Thrift Beacon – Home</title>
<link href="https://fonts.googleapis.com/css2?family=Open+Sans:ital,wght@0,400;0,600;0,700;0,800;1,400;1,600&display=swap" rel="stylesheet">
<style>
:root{
  --orange:#ef7d22;
  --orange-dark:#d96a12;
  --orange-pale:#fbe3cf;
  --green:#4f7a3a;
  --ink:#333;
  --muted:#777;
  --line:#e2e2e2;
  --card:#f4f4f4;
  --footer:#23272b;
  --footer-base:#1a1d20;
  --white:#fff;
}
*{box-sizing:border-box;margin:0;padding:0}
html,body{width:741px;height:1200px;overflow:hidden;background:var(--white)}
body{font-family:"Open Sans",Arial,sans-serif;color:var(--ink);position:relative}

.topbar{height:66px;display:flex;align-items:center;justify-content:space-between;padding:0 18px;font-size:10px;color:var(--muted)}
.contact p{line-height:15px}
.brand{display:flex;align-items:center;gap:7px;font-weight:700;font-size:19px;color:#444;position:absolute;left:50%;top:20px;transform:translateX(-50%)}
.brand-dot{width:22px;height:22px;border-radius:50%;background:var(--orange)}
.account-links{display:flex;gap:14px}
.account-links a{color:var(--muted);text-decoration:none}
.account-links a.accent{color:var(--orange)}

.mainnav{height:24px;background:var(--orange);display:flex;justify-content:space-between;padding:0 22px;align-items:center}
.mainnav a{color:var(--white);font-size:9.5px;font-weight:600;text-decoration:none}

.hero{height:265px;position:relative;background:linear-gradient(100deg,#4a4541 0%,#6d665f 45%,#3b3836 100%);overflow:hidden}
.hero-photo{position:absolute;inset:0}
.hero-copy{position:absolute;left:150px;top:88px;color:var(--white)}
.hero-copy h1{font-size:22px;font-weight:800;font-style:italic;letter-spacing:.2px;margin-bottom:10px}
.hero-copy li{list-style:none;font-size:12px;font-style:italic;font-weight:600;line-height:20px;display:flex;align-items:center;gap:8px}
.hero-arrow{position:absolute;top:118px;width:20px;height:30px}
.hero-arrow.prev{left:12px}.hero-arrow.next{right:12px}

.signup{position:absolute;left:180px;top:370px;width:384px;height:66px;background:var(--orange-pale);padding:14px;display:flex;gap:8px}
.signup .field{flex:1;background:var(--white);border:1px solid var(--line);font-size:9.5px;color:#999;display:flex;align-items:center;padding-left:12px}
.signup .btn{background:var(--orange);color:var(--white);font-size:10px;font-weight:700;display:flex;align-items:center;padding:0 14px}

.advice{position:absolute;top:460px;left:0;width:741px}
.advice h2{text-align:center;font-size:13px;font-weight:700;letter-spacing:1px;color:#444}
.cards{display:flex;gap:22px;padding:0 34px;margin-top:14px}
.card{flex:1;text-align:center}
.card-icon{height:44px;display:flex;justify-content:center;align-items:center;margin-bottom:8px}
.card-head{height:26px;line-height:26px;font-size:10px;font-weight:700;background:var(--card);color:#555;border:1px solid var(--line)}
.card-head.feature{background:var(--green);color:var(--white);border-color:var(--green)}
.card-body{border:1px solid var(--line);border-top:0;padding:12px 14px 12px;height:130px;display:flex;flex-direction:column;justify-content:space-between}
.card-body p{text-align:left;font-size:9.5px;line-height:14px;color:#555}
.card-btn{border:1px solid #ccc;font-size:9px;color:#555;padding:5px 0;border-radius:2px}

.testimonial{position:absolute;top:735px;left:0;width:741px;height:150px;background:var(--orange);color:var(--white);text-align:center;padding:22px 60px 0}
.testimonial blockquote{font-size:10.5px;font-style:italic;line-height:16px}
.testimonial .name{font-size:13px;font-weight:700;margin-top:10px}
.testimonial .role{font-size:8.5px}
.dots{display:flex;justify-content:center;gap:5px;margin-top:7px}
.dots span{width:6px;height:6px;border-radius:50%;background:rgba(255,255,255,.5)}
.dots span.on{background:var(--white)}
.qmark{position:absolute;top:8px;font-size:48px;font-weight:800;line-height:1;color:rgba(255,255,255,.55)}

.press{position:absolute;top:900px;left:0;width:741px;height:70px;display:flex;align-items:center;gap:12px;padding:0 8px}
.press-arrow{width:18px;height:28px;background:var(--orange);display:flex;align-items:center;justify-content:center}
.press-badges{flex:1;display:flex;gap:12px}
.press-badges span{flex:1;height:40px;background:#d9d9d9;border-radius:2px}

.footer{position:absolute;top:985px;left:0;width:741px;height:175px;background:var(--footer);color:#bbb;display:flex;padding:26px 30px 0}
.footer .brand{position:static;transform:none;color:var(--white);font-size:17px;width:200px;align-self:flex-start;margin-top:40px}
.footer h3{font-size:10px;color:var(--white);font-weight:700;letter-spacing:.5px;margin-bottom:10px}
.links{width:270px}
.links .cols{display:flex;gap:24px}
.links ul{list-style:none}
.links li{font-size:8.5px;line-height:17px}
.newsletter{flex:1}
.newsletter p{font-size:8.5px;line-height:13px;margin-bottom:10px}
.nl-form{display:flex;height:22px}
.nl-form .field{flex:1;background:var(--white);font-size:8px;color:#999;display:flex;align-items:center;padding-left:8px}
.nl-form .btn{width:30px;background:var(--orange);color:var(--white);font-size:9px;font-weight:700;display:flex;align-items:center;justify-content:center}

.legal{position:absolute;top:1160px;left:0;width:741px;height:40px;background:var(--footer-base);color:#888;font-size:8px;text-align:center;padding-top:9px;line-height:12px}
</style>
</head>
<body>

<header class="topbar">
  <div class="contact">
    <p>0800 555 0142</p>
    <p>info@thriftbeacon.co.uk</p>
  </div>
  <div class="brand"><span class="brand-dot"></span>Thrift Beacon</div>
  <nav class="account-links"><a href="#">Register Now</a><a href="#" class="accent">Login</a><a href="#">Help</a></nav>
</header>

<nav class="mainnav">
  <a href="#">Concierge Service</a><a href="#">Best Buy Tables</a><a href="#">Rate Tracker®</a><a href="#">News and Alerts</a><a href="#">Advice and Guides</a><a href="#">Awards</a><a href="#">About Us</a>
</nav>

<section class="hero">
  <div class="hero-photo" role="img" aria-label="Photo of a team of advisers in a bright office"></div>
  <svg class="hero-arrow prev" viewBox="0 0 20 30"><path d="M14 4 4 15l10 11" fill="none" stroke="#fff" stroke-width="3"/></svg>
  <svg class="hero-arrow next" viewBox="0 0 20 30"><path d="M6 4l10 11-10 11" fill="none" stroke="#fff" stroke-width="3"/></svg>
  <div class="hero-copy">
    <h1>GET FREE WHOLE OF MARKET INFORMATION:</h1>
    <ul>
      <li><svg width="11" height="10" viewBox="0 0 11 10"><path d="M1 5l3 3 6-7" fill="none" stroke="#fff" stroke-width="2"/></svg>Uncompromised Best Buy Tables</li>
      <li><svg width="11" height="10" viewBox="0 0 11 10"><path d="M1 5l3 3 6-7" fill="none" stroke="#fff" stroke-width="2"/></svg>Account Monitoring and Alert Services</li>
      <li><svg width="11" height="10" viewBox="0 0 11 10"><path d="M1 5l3 3 6-7" fill="none" stroke="#fff" stroke-width="2"/></svg>Access to Savings Experts</li>
    </ul>
  </div>
</section>

<form class="signup">
  <div class="field">Enter Your email address</div>
  <div class="btn">Choose your free services</div>
</form>

<section class="advice">
  <h2>SPECIALIST ADVICE</h2>
  <div class="cards">
    <article class="card">
      <div class="card-icon"><svg width="36" height="36" viewBox="0 0 36 36" fill="var(--green)"><circle cx="12" cy="12" r="7"/><circle cx="24" cy="12" r="7"/><circle cx="12" cy="24" r="7"/><circle cx="24" cy="24" r="7"/></svg></div>
      <div class="card-head feature">£100,000 PLUS IN SAVINGS?</div>
      <div class="card-body"><p>Find out how we've doubled the returns for savers. Download your free guide</p><div class="card-btn">would you like to know more?</div></div>
    </article>
    <article class="card">
      <div class="card-icon"><svg width="38" height="34" viewBox="0 0 38 34" fill="#666"><rect x="2" y="22" width="6" height="10"/><rect x="11" y="16" width="6" height="16"/><rect x="20" y="10" width="6" height="22"/><rect x="29" y="4" width="6" height="28"/><rect x="0" y="32" width="38" height="2"/></svg></div>
      <div class="card-head">WEALTH MANAGEMENT</div>
      <div class="card-body"><p>Find out how to get the best advice for your pensions, investments and financial planning.</p><div class="card-btn">would you like to know more?</div></div>
    </article>
    <article class="card">
      <div class="card-icon"><svg width="30" height="38" viewBox="0 0 30 38" fill="none" stroke="#666" stroke-width="2"><path d="M15 3a10 10 0 0 0-6 18v5h12v-5A10 10 0 0 0 15 3z"/><path d="M10 30h10M11 34h8"/></svg></div>
      <div class="card-head">TAKE OUR £50 CHALLENGE</div>
      <div class="card-body"><p>If you have over £100,000 on deposit, go compare and we can improve your savings situation or we will donate £50 to a charity of your choice if we can't.</p><div class="card-btn">would you like to know more?</div></div>
    </article>
  </div>
</section>

<section class="testimonial">
  <span class="qmark" style="left:20px">“</span><span class="qmark" style="right:20px">”</span>
  <blockquote>Thrift Beacon's treasure trove of data is one of my most valued sources of information on savings products. Thrift Beacon is the best innovation in savings I have seen in recent years – comprehensive rate tracking, coupled with wide-ranging help in finding better deals is exactly what savers need.</blockquote>
  <p class="name">Milo Hartley</p>
  <p class="role">Deputy Personal Finance Editor, Ledger Media Group</p>
  <div class="dots"><span class="on"></span><span></span><span></span><span></span><span></span></div>
</section>

<section class="press">
  <div class="press-arrow"><svg width="8" height="12" viewBox="0 0 8 12"><path d="M6 1 1 6l5 5" fill="none" stroke="#fff" stroke-width="2"/></svg></div>
  <div class="press-badges"><span></span><span></span><span></span><span></span><span></span><span></span></div>
  <div class="press-arrow"><svg width="8" height="12" viewBox="0 0 8 12"><path d="M2 1l5 5-5 5" fill="none" stroke="#fff" stroke-width="2"/></svg></div>
</section>

<footer class="footer">
  <div class="brand"><span class="brand-dot"></span>Thrift Beacon</div>
  <div class="links">
    <h3>TOP SAVINGS ACCOUNTS</h3>
    <div class="cols">
      <ul><li>High Interest Current Accounts</li><li>Instant Easy Ads</li><li>Monthly Income</li><li>Easy Access</li><li>Fixed Rate Bonds</li></ul>
      <ul><li>Fixed Rate ISAs</li><li>Notice Accounts</li><li>Regular Savings</li><li>Children's Accounts</li></ul>
    </div>
  </div>
  <div class="newsletter">
    <h3>NEWSLETTER</h3>
    <p>Stay in the loop with our savings roundup: rates, tips and the best deals delivered to your inbox each week.</p>
    <div class="nl-form"><div class="field">Enter your email address</div><div class="btn">OK</div></div>
  </div>
</footer>

<div class="legal">
  <p>Terms &amp; Conditions | Privacy Policy | Cookie Policy | Website Security</p>
  <p>© 2016 Thrift Beacon Ltd. All rights reserved.</p>
</div>

</body>
</html>
```